Design für meine Gesichtscreme
Zielgruppe
Kosmetikprodukte für Frauen, zwischen 35-50,
Aufgabenstellung
ich kann nur 1färbig drucken, bitte berücksichtigen!
der Name ' Solvetra' muss mit drauf,das ist die neue Marke. Es soll als Logo auffallen ( andere Schriftart und mit einem Blatt oder Blume oder Schnörkel versehen werden.)
Lindhavel Pflegekosmetik heißt meine Firma.
Ich habe meine derzeitigen Verpackungen dazu gefügt. Das Design gefällt mir vom Stil gut,'Solvetra' soll bitte noch eingearbeitet werden. Vielen Dank!

```html
<!DOCTYPE html>
<html lang="de">
<head>
<meta charset="utf-8">
<title>Solvetra Hautbalsam – Farbvarianten</title>
<link rel="stylesheet" href="https://fonts.googleapis.com/css2?family=Marcellus&display=swap">
<style>
  :root {
    --canvas: #e6e4e0;
    --label: #f3f2ef;
    --label-edge: #d9d7d2;
    --ink: #111111;
    --taupe: #6b625c;
    --gold: #b0a263;
    --mauve: #7a6176;
    --band-text: #f1efea;
  }
  * { margin: 0; padding: 0; box-sizing: border-box; }
  html, body { width: 1200px; height: 1200px; overflow: hidden; }
  body {
    background: var(--canvas);
    font-family: "Marcellus", "Times New Roman", serif;
    position: relative;
  }
  .variant { position: absolute; top: 290px; }
  .variant--taupe { left: 80px;  --tone: var(--taupe); }
  .variant--gold  { left: 432px; --tone: var(--gold); }
  .variant--mauve { left: 786px; --tone: var(--mauve); }

  .variant-number {
    position: absolute;
    top: 395px;
    left: -50px;
    font-size: 58px;
    color: var(--ink);
    line-height: 1;
  }
  .label {
    width: 252px;
    height: 825px;
    background: var(--label);
    border: 1px solid var(--label-edge);
    border-radius: 12px 12px 18px 18px;
    position: relative;
  }
  .label__mark {
    position: absolute;
    top: 118px;
    left: 0; right: 0;
    text-align: center;
    font-size: 34px;
    color: var(--tone);
  }
  .label__divider {
    position: absolute;
    top: 258px;
    left: 0; right: 0;
    height: 1px;
    background: var(--label-edge);
  }
  .label__band {
    position: absolute;
    top: 335px;
    left: 50%;
    width: 48px;
    height: 375px;
    margin-left: -6px;
    background: var(--tone);
    display: flex;
    align-items: center;
    justify-content: center;
  }
  .label__product {
    writing-mode: vertical-rl;
    transform: rotate(180deg);
    font-size: 33px;
    letter-spacing: 0.2em;
    color: var(--band-text);
    line-height: 1;
  }
  .label__brand {
    position: absolute;
    top: 718px;
    left: 0; right: 0;
    text-align: center;
    color: var(--tone);
  }
  .label__brand-name {
    display: block;
    font-size: 30px;
    line-height: 1.1;
  }
  .label__brand-rule {
    display: block;
    width: 178px;
    height: 1px;
    margin: 4px auto 5px;
    background: var(--tone);
  }
  .label__company {
    display: block;
    font-size: 17px;
    letter-spacing: 0.22em;
  }
</style>
</head>
<body>
  <section class="variant variant--taupe">
    <span class="variant-number">1</span>
    <div class="label">
      <div class="label__mark">Solvetra</div>
      <div class="label__divider"></div>
      <div class="label__band"><span class="label__product">HAUTBALSAM</span></div>
      <div class="label__brand">
        <span class="label__brand-name">Solvetra</span>
        <span class="label__brand-rule"></span>
        <span class="label__company">LINDHAVEL</span>
      </div>
    </div>
  </section>

  <section class="variant variant--gold">
    <span class="variant-number">2</span>
    <div class="label">
      <div class="label__mark">Solvetra</div>
      <div class="label__divider"></div>
      <div class="label__band"><span class="label__product">HAUTBALSAM</span></div>
      <div class="label__brand">
        <span class="label__brand-name">Solvetra</span>
        <span class="label__brand-rule"></span>
        <span class="label__company">LINDHAVEL</span>
      </div>
    </div>
  </section>

  <section class="variant variant--mauve">
    <span class="variant-number">3</span>
    <div class="label">
      <div class="label__mark">Solvetra</div>
      <div class="label__divider"></div>
      <div class="label__band"><span class="label__product">HAUTBALSAM</span></div>
      <div class="label__brand">
        <span class="label__brand-name">Solvetra</span>
        <span class="label__brand-rule"></span>
        <span class="label__company">LINDHAVEL</span>
      </div>
    </div>
  </section>
</body>
</html>
```